Harborline I.T.
Harborline I.T. -
Creative Brief
Modern
Daniel Whitcombe
Owner
1875 Crandall Brook Ct. Lindenvale, OR 97390
dwhitcombe@harbolintech.example
Can use either business name on cards (Harborline I.T. --- or --- Harborline Information Technologies) whichever works best for you.

```html
<!DOCTYPE html>
<html lang="en">
<head>
<meta charset="utf-8">
<title>Harborline I.T. – Business Card</title>
<link href="https://fonts.googleapis.com/css2?family=Open+Sans:wght@400;600;700&display=swap" rel="stylesheet">
<style>
  :root {
    --backdrop: #2b2b2d;
    --card: #ffffff;
    --brand-blue: #1f63b8;
    --swoosh-blue: #2a6fc4;
    --swoosh-deep: #164f96;
    --swoosh-grey: #5d6068;
    --text-dark: #2f3237;
    --divider: #c7cad0;
  }
  * { margin: 0; padding: 0; box-sizing: border-box; }
  html, body { width: 1200px; height: 596px; overflow: hidden; }
  body {
    background: var(--backdrop);
    font-family: "Open Sans", Arial, sans-serif;
    position: relative;
  }
  .card {
    position: absolute;
    top: 150px;
    width: 510px;
    height: 292px;
    background: var(--card);
    border-radius: 14px;
    overflow: hidden;
    box-shadow: 0 6px 18px rgba(0,0,0,0.45);
  }
  .card--front { left: 70px; }
  .card--back { left: 620px; }

  .brand {
    position: absolute;
    display: flex;
    align-items: center;
    gap: 8px;
    color: var(--brand-blue);
    font-weight: 700;
    letter-spacing: 0.5px;
    white-space: nowrap;
  }
  .brand__dot {
    width: 14px; height: 14px;
    border-radius: 50%;
    background: var(--brand-blue);
  }
  .card--front .brand { left: 26px; top: 58px; font-size: 22px; }
  .card--back .brand { left: 150px; top: 126px; font-size: 24px; }

  .holder { position: absolute; left: 26px; top: 152px; }
  .holder__name { color: var(--brand-blue); font-weight: 700; font-size: 15px; }
  .holder__role { color: var(--text-dark); font-size: 12px; margin-top: 1px; }

  .contact {
    position: absolute;
    left: 284px; top: 134px;
    padding-left: 9px;
    border-left: 1px solid var(--divider);
    font-size: 9.5px;
    line-height: 14px;
    color: var(--text-dark);
    white-space: nowrap;
  }

  .swoosh { position: absolute; left: 0; bottom: 0; width: 510px; height: 80px; }

  .back-shade {
    position: absolute;
    right: 0; top: 0;
    width: 200px; height: 160px;
    background: radial-gradient(circle at 100% 0%, rgba(200,212,230,0.45), rgba(255,255,255,0) 70%);
  }
</style>
</head>
<body>
  <section class="card card--front" aria-label="Card front">
    <div class="brand"><span class="brand__dot"></span>Harborline I.T.</div>
    <div class="holder">
      <div class="holder__name">Daniel Whitcombe</div>
      <div class="holder__role">Owner</div>
    </div>
    <div class="contact">
      1875 Crandall Brook Ct.<br>
      Lindenvale, OR 97390<br>
      Phone: 555 010 0142<br>
      Fax: 555 010 0187<br>
      Email: dwhitcombe@harbolintech.example
    </div>
    <svg class="swoosh" viewBox="0 0 510 80" preserveAspectRatio="none">
      <path d="M0 30 C140 6 300 4 510 18 L510 26 C300 14 150 18 0 44 Z" fill="var(--swoosh-grey)"/>
      <path d="M0 50 C150 24 320 20 510 34 L510 80 L0 80 Z" fill="var(--swoosh-blue)"/>
      <path d="M0 62 C170 40 330 40 510 54 L510 80 L0 80 Z" fill="var(--swoosh-deep)"/>
    </svg>
  </section>

  <section class="card card--back" aria-label="Card back">
    <div class="back-shade"></div>
    <div class="brand"><span class="brand__dot"></span>Harborline I.T.</div>
  </section>
</body>
</html>
```